Wholesale Janitorial supply company needs promotional postcard

We need a postcard designed to entice old customers who stopped buying their janitorial and maintenance supplies( cleaning chemicals, paper supplies, etc) from us. We wanted a "we missed you" type theme, offering a 15% discount on your next order of $300.00 or more. Colors are green with black and white accents. Our website is tormisk.com, it will give you a better understanding of exactly who we are.

Industry/Entity Type

It Company

Font styles to use
Sans Serif

```html
<!DOCTYPE html>
<html lang="en">
<head>
<meta charset="utf-8">
<title>Tormisk Supply Company – We've Missed You Postcard</title>
<link rel="stylesheet" href="https://fonts.googleapis.com/css2?family=Arimo:wght@400;700&family=Josefin+Sans:wght@300&family=Montserrat:wght@900&display=swap">
<style>
  :root {
    --green: #137a3c;
    --green-deep: #0b3a1e;
    --ink: #111111;
    --paper: #ffffff;
    --paper-soft: #eef0ef;
    --teal-mist: #d7ebe6;
    --teal-light: #f2f8f6;
  }
  * { margin: 0; padding: 0; box-sizing: border-box; }
  html, body { width: 1200px; height: 750px; overflow: hidden; background: var(--paper); }
  .postcard {
    position: relative; width: 1200px; height: 750px; overflow: hidden;
    background: var(--paper);
    font-family: "Arimo", Arial, sans-serif; color: var(--ink);
  }
  .backdrop { position: absolute; inset: 0; }
  .brand { position: absolute; left: 40px; top: 40px; display: flex; align-items: center; gap: 14px; }
  .brand-dot { width: 52px; height: 52px; border-radius: 50%; background: var(--green); }
  .brand-name { font-weight: 700; font-size: 34px; color: var(--green); }
  .contact { position: absolute; right: 50px; top: 30px; text-align: right; line-height: 1; }
  .contact-label { font-size: 26px; font-weight: 700; letter-spacing: 0.5px; }
  .contact-tollfree { font-size: 50px; font-weight: 700; color: var(--green); margin-top: 6px; }
  .contact-local { font-size: 40px; margin-top: 4px; }
  .tagline {
    position: absolute; left: 330px; top: 178px; right: 40px;
    color: var(--paper); font-size: 22px; letter-spacing: 0.6px;
  }
  .photo {
    position: absolute; left: 90px; top: 240px; width: 510px; height: 460px;
    background: radial-gradient(ellipse at 50% 40%, #c9dbe9 0%, #8fb0cc 45%, #e9d26a 80%, transparent 100%);
    border-radius: 40px 40px 0 0;
  }
  .web-ribbon {
    position: absolute; left: 0; top: 520px; width: 380px; height: 58px;
    background: var(--ink); color: var(--paper);
    font-weight: 700; font-size: 30px; line-height: 58px; padding-left: 40px;
    clip-path: polygon(0 0, 100% 0, 92% 50%, 100% 100%, 0 100%);
  }
  .headline {
    position: absolute; left: 610px; top: 350px; width: 560px; text-align: center;
    font-family: "Josefin Sans", Arial, sans-serif; font-weight: 300;
    font-size: 72px; line-height: 0.95; letter-spacing: 3px;
  }
  .discount {
    position: absolute; left: 660px; top: 505px; display: flex; align-items: flex-start;
    font-family: "Montserrat", Arial, sans-serif; font-weight: 900; color: var(--green);
  }
  .discount-figure { font-size: 180px; line-height: 0.85; letter-spacing: -8px; }
  .discount-unit { display: flex; flex-direction: column; margin-left: 14px; line-height: 0.9; }
  .discount-percent { font-size: 90px; }
  .discount-off { font-size: 60px; }
  .offer-terms {
    position: absolute; left: 560px; top: 688px; width: 620px; text-align: center;
    font-size: 28px; font-weight: 700;
  }
  .offer-terms .amount { color: var(--green); }
</style>
</head>
<body>
<main class="postcard">
  <svg class="backdrop" width="1200" height="750" viewBox="0 0 1200 750" aria-hidden="true">
    <defs>
      <linearGradient id="deep-panel" x1="0" y1="0" x2="1" y2="1">
        <stop offset="0" stop-color="#0b3a1e"/>
        <stop offset="1" stop-color="#151c18"/>
      </linearGradient>
      <linearGradient id="mist-panel" x1="0" y1="0" x2="1" y2="0">
        <stop offset="0" stop-color="#f2f8f6"/>
        <stop offset="1" stop-color="#cfe6df"/>
      </linearGradient>
      <linearGradient id="lower-panel" x1="0" y1="0" x2="0" y2="1">
        <stop offset="0" stop-color="#ffffff"/>
        <stop offset="1" stop-color="#eef0ef"/>
      </linearGradient>
    </defs>
    <rect x="0" y="150" width="1200" height="320" fill="url(#mist-panel)"/>
    <path d="M0 150 H640 L620 470 H0 Z" fill="url(#deep-panel)"/>
    <path d="M0 455 C350 380 750 300 1200 265 V750 H0 Z" fill="url(#lower-panel)"/>
    <path d="M0 455 C350 380 750 300 1200 265" fill="none" stroke="#111111" stroke-width="14"/>
    <rect x="0" y="165" width="1200" height="48" fill="#111111"/>
    <rect x="0" y="0" width="1200" height="150" fill="#ffffff"/>
    <path d="M560 0 H1200 V150 H470 Z" fill="url(#mist-panel)"/>
  </svg>

  <div class="brand">
    <span class="brand-dot"></span>
    <span class="brand-name">Tormisk Supply Company</span>
  </div>

  <div class="contact">
    <p class="contact-label">CALL US TOLL FREE</p>
    <p class="contact-tollfree">1-800-555-0142</p>
    <p class="contact-local">or 555-201-3478</p>
  </div>

  <p class="tagline">Providing Total Solutions for a Clean, Healthy, Safe Environment</p>

  <div class="photo" role="img" aria-label="Smiling woman in a blue blouse presenting the offer, with colourful cleaning product bottles behind her"></div>

  <div class="web-ribbon">www.tormisk.com</div>

  <h1 class="headline">WE'VE<br>MISSED YOU</h1>

  <div class="discount">
    <span class="discount-figure">15</span>
    <span class="discount-unit">
      <span class="discount-percent">%</span>
      <span class="discount-off">OFF</span>
    </span>
  </div>

  <p class="offer-terms">On Your Next Order Of <span class="amount">$300</span> Or More</p>
</main>
</body>
</html>
```